Billboard Design for Harbor Lane Dentistry

Brookhaven Family Dental Care
Phone number: 318-562-0913
Address: 248 Castleford Blvd
Hours: 7am-5pm ; Monday-Friday

Dental Implant Surgery
Same Day Emergency Visits
Cosmetic Treatments
GLINT! Whitening

NAMES: Dr. Colin Varnstaad
Dr. Peter Ashdale

MOST INSURANCES ACCEPTED

Eye catching slogan/colors/design for billboard

Our website is www.brookhavenfamilydentalcare.example to see current branding.

Target Market(s)

Target market is anyone in Alexandria. Focus on Families and High End Cosmetic Dentistry.

Industry/Entity Type

Dental Clinic

Requirements
Must have
• Brookhaven Family Dental Care
• Phone number: 318-562-0913
• Address: 248 Castleford Blvd
• Hours: 7am-5pm ; Monday-Friday
• Dental Implant Surgery
• Same Day Emergency Visits
• Cosmetic Treatments
• GLINT! Whitening
• NAMES: Dr. Colin Varnstaad
• Dr. Peter Ashdale
• and logo
Nice to have
• digital billboard-try to catch attention with color or phrase
Should not have
• Can not make claims or compare to other area dentist's according to laws.

```html
<!DOCTYPE html>
<html lang="en">
<head>
<meta charset="utf-8">
<title>Harbor Lane Dentistry – Billboard</title>
<link rel="stylesheet" href="https://fonts.googleapis.com/css2?family=Montserrat:wght@500;600;800&family=Quicksand:wght@400&family=PT+Sans:wght@400;700&display=swap">
<style>
  :root{
    --teal:#1bb6cc;
    --teal-deep:#0f9fb8;
    --band:#0f7fb3;
    --royal:#0b4fd1;
    --navy-text:#1f4fae;
    --ink:#1b2736;
    --grey:#5a5d62;
    --silver:#a9adb2;
    --page:#eef1f5;
    --white:#ffffff;
  }
  *{box-sizing:border-box;margin:0;padding:0}
  html,body{width:1200px;height:1120px;overflow:hidden}
  body{background:var(--page);position:relative;font-family:"PT Sans",sans-serif}
  .billboard{position:absolute;left:20px;top:255px;width:1160px;height:610px;background:var(--white);overflow:hidden;box-shadow:0 6px 24px rgba(0,0,0,.12)}
  .billboard-art{position:absolute;inset:0}
  .brand-lockup{position:absolute;left:100px;top:40px;width:360px;text-align:center;color:var(--teal);font-family:"Montserrat",sans-serif;font-weight:600}
  .brand-mark{display:block;width:54px;height:54px;border-radius:50%;background:var(--teal);margin:0 auto 10px}
  .brand-name{display:block;font-size:40px;letter-spacing:1px;line-height:1}
  .brand-sub{display:block;font-size:13px;letter-spacing:8px;margin-top:6px}
  .panel{position:absolute;left:670px;width:470px;text-align:center}
  .headline{top:56px;font-family:"Montserrat",sans-serif;font-weight:600;font-size:56px;color:var(--teal);letter-spacing:1px;line-height:1}
  .subhead{top:120px;font-family:"Quicksand",sans-serif;font-size:44px;color:var(--grey);line-height:1.1}
  .doctors{top:190px;font-weight:700;font-size:20px;color:var(--navy-text);display:flex;justify-content:center;align-items:center;gap:10px}
  .doctors .sep{width:8px;height:8px;background:var(--teal);display:inline-block}
  .services{top:232px;height:134px;background:var(--teal);border-radius:10px;overflow:hidden;color:var(--white)}
  .service-list{display:grid;grid-template-columns:1.1fr 1fr;gap:6px 8px;padding:14px 14px 0;list-style:none;text-align:left;font-size:16px}
  .service-list li{white-space:nowrap}
  .service-list li::before{content:"\2713\00a0";font-weight:700}
  .insurance{position:absolute;left:0;right:0;bottom:0;height:50px;background:var(--band);font-family:"Montserrat",sans-serif;font-weight:500;font-size:24px;line-height:50px}
  .address{top:384px;font-weight:700;font-size:22px;color:var(--ink);display:flex;justify-content:center;align-items:center;gap:8px}
  .hours{top:418px;font-size:24px;color:var(--navy-text)}
  .call{top:508px;font-family:"Montserrat",sans-serif;font-weight:800;font-size:44px;color:var(--white);line-height:1}
  .website{top:565px;font-family:"Montserrat",sans-serif;font-weight:500;font-size:18px;color:var(--white)}
</style>
</head>
<body>
<main class="billboard">
  <svg class="billboard-art" viewBox="0 0 1160 610" width="1160" height="610">
    <defs>
      <linearGradient id="photoTone" x1="0" y1="0" x2="0" y2="1">
        <stop offset="0" stop-color="#ffffff"/>
        <stop offset=".35" stop-color="#efe3d8"/>
        <stop offset=".7" stop-color="#e2c8b3"/>
        <stop offset="1" stop-color="#f1f2f4"/>
      </linearGradient>
      <linearGradient id="tealFill" x1="0" y1="0" x2="1" y2="0">
        <stop offset="0" stop-color="var(--teal-deep)"/>
        <stop offset=".6" stop-color="#2cc3d8"/>
        <stop offset="1" stop-color="var(--teal-deep)"/>
      </linearGradient>
    </defs>
    <path role="img" aria-label="Photo of a smiling family of four relaxing together on a white bed" d="M0 180 L520 180 C600 300 610 440 520 610 L0 610 Z" fill="url(#photoTone)"/>
    <path class="footer-wave" d="M560 610 L600 482 C700 500 900 510 1000 500 C1080 492 1130 480 1160 472 L1160 610 Z" fill="url(#tealFill)"/>
    <path class="footer-rule" d="M600 474 C700 492 900 502 1000 492 C1080 484 1130 472 1160 464" fill="none" stroke="var(--silver)" stroke-width="10"/>
    <path class="swoosh-silver" d="M505 0 C620 130 640 360 515 610" fill="none" stroke="var(--silver)" stroke-width="14"/>
    <path class="swoosh-royal" d="M542 0 C660 140 680 360 552 610" fill="none" stroke="var(--royal)" stroke-width="26"/>
  </svg>

  <div class="brand-lockup">
    <span class="brand-mark"></span>
    <span class="brand-name">BROOKHAVEN</span>
    <span class="brand-sub">FAMILY DENTAL CARE</span>
  </div>

  <h1 class="panel headline">BROOKHAVEN</h1>
  <p class="panel subhead">Family Dental Care</p>
  <p class="panel doctors"><span>Dr. Colin Varnstaad</span><span class="sep"></span><span>Dr. Peter Ashdale</span></p>

  <section class="panel services">
    <ul class="service-list">
      <li>Dental Implant Surgery</li>
      <li>Cosmetic Treatments</li>
      <li>Same Day Emergency Visits</li>
      <li>GLINT! Whitening</li>
    </ul>
    <p class="insurance">MOST INSURANCES ACCEPTED</p>
  </section>

  <p class="panel address">
    <svg width="14" height="20" viewBox="0 0 14 20" aria-hidden="true"><path d="M7 1a6 6 0 0 1 6 6c0 4.5-6 12-6 12S1 11.5 1 7a6 6 0 0 1 6-6z" fill="none" stroke="var(--navy-text)" stroke-width="2"/><circle cx="7" cy="7" r="2" fill="var(--navy-text)"/></svg>
    <span>248 Castleford Blvd</span>
  </p>
  <p class="panel hours">7AM-5PM ; MONDAY-FRIDAY</p>
  <p class="panel call">CALL : 318-562-0913</p>
  <p class="panel website">www.brookhavenfamilydentalcare.example</p>
</main>
</body>
</html>
```